A online shop for solid wood need a Stationary design

A new online shop (in Austria and Germany) for solid wood and steel furniture (feldberg-formwerk) needs a Stationay design (letterhead, business card, envelope etc...). Dining tables, coffee tables, TV furniture and similar furniture will be sold. Everything will be custom made.

```html
<!DOCTYPE html>
<html lang="en">
<head>
<meta charset="utf-8">
<title>Feldberg Formwerk – Business Card</title>
<link href="https://fonts.googleapis.com/css2?family=Arimo:wght@400;700&display=swap" rel="stylesheet">
<style>
  :root {
    --stage: #2b2b2b;
    --card: #222222;
    --card-deep: #151515;
    --brand-red: #e41e26;
    --text-light: #f2f2f2;
    --text-muted: #b9b9b9;
    --rule: #e6e6e6;
  }
  * { margin: 0; padding: 0; box-sizing: border-box; }
  html, body { width: 1200px; height: 874px; overflow: hidden; }
  body {
    background: var(--stage);
    font-family: "Arimo", Arial, sans-serif;
    position: relative;
  }
  .card {
    position: absolute;
    left: 310px;
    width: 580px;
    height: 332px;
    background: var(--card);
    border-radius: 22px;
    overflow: hidden;
  }
  .card--front { top: 84px; }
  .card--back { top: 458px; }

  /* front */
  .front__decoration {
    position: absolute;
    left: 0; top: 0;
    width: 330px; height: 100%;
    background: linear-gradient(160deg, var(--card-deep) 0%, #1b1b1b 45%, #4a4a4a 100%);
  }
  .brand-name {
    color: var(--brand-red);
    font-weight: 700;
    text-transform: uppercase;
    line-height: 1;
  }
  .brand-name__primary { display: block; font-size: 40px; letter-spacing: 2px; }
  .brand-name__secondary { display: block; font-size: 13px; letter-spacing: 6.2px; margin-top: 6px; }
  .front__brand { position: absolute; right: 34px; bottom: 40px; text-align: left; }

  /* back */
  .holder { position: absolute; left: 40px; top: 48px; }
  .holder__name { color: var(--brand-red); font-weight: 700; font-size: 26px; }
  .holder__role { color: var(--text-light); font-size: 16px; margin-top: 2px; }
  .back__rule {
    position: absolute; left: 40px; right: 40px; top: 178px;
    height: 1px; background: var(--rule);
  }
  .contact { position: absolute; left: 40px; top: 106px; list-style: none; }
  .contact__item {
    display: flex; align-items: center; gap: 10px;
    color: var(--text-light); font-size: 17px; height: 22px;
  }
  .contact__item svg { width: 14px; height: 14px; flex: none; }
  .back__brand { position: absolute; right: 40px; top: 54px; display: flex; align-items: center; gap: 14px; }
  .brand-mark-square { width: 54px; height: 54px; background: var(--brand-red); border-radius: 6px; }
  .address {
    position: absolute; right: 40px; top: 196px;
    color: var(--text-light); font-size: 17px; line-height: 1.3; text-align: right;
  }
</style>
</head>
<body>
  <section class="card card--front" aria-label="Business card front">
    <div class="front__decoration" role="img" aria-label="Large embossed brand-mark decoration in dark glossy tones"></div>
    <div class="front__brand brand-name">
      <span class="brand-name__primary">Feldberg</span>
      <span class="brand-name__secondary">Formwerk</span>
    </div>
  </section>

  <section class="card card--back" aria-label="Business card back">
    <div class="holder">
      <p class="holder__name">Lukas Brenner</p>
      <p class="holder__role">Manager</p>
    </div>
    <ul class="contact">
      <li class="contact__item">
        <svg viewBox="0 0 24 24" fill="var(--brand-red)"><path d="M6.6 10.8a15 15 0 0 0 6.6 6.6l2.2-2.2a1 1 0 0 1 1-.25 11.4 11.4 0 0 0 3.6.57 1 1 0 0 1 1 1V20a1 1 0 0 1-1 1A17 17 0 0 1 3 4a1 1 0 0 1 1-1h3.5a1 1 0 0 1 1 1c0 1.25.2 2.45.57 3.57a1 1 0 0 1-.25 1z"/></svg>
        123-456-2100
      </li>
      <li class="contact__item">
        <svg viewBox="0 0 24 24" fill="var(--brand-red)"><path d="M2 5h20v14H2z"/><path d="M2 5l10 8 10-8" fill="none" stroke="#222" stroke-width="1.6"/></svg>
        mail@feldberg-formwerk.at
      </li>
      <li class="contact__item">
        <svg viewBox="0 0 24 24"><circle cx="12" cy="12" r="10" fill="var(--brand-red)"/><path d="M2 12h20M12 2c3 3 3 17 0 20M12 2c-3 3-3 17 0 20" stroke="#222" stroke-width="1.4" fill="none"/></svg>
        www.feldberg-formwerk.at
      </li>
    </ul>
    <div class="back__brand">
      <span class="brand-mark-square" aria-hidden="true"></span>
      <div class="brand-name">
        <span class="brand-name__primary">Feldberg</span>
        <span class="brand-name__secondary">Formwerk</span>
      </div>
    </div>
    <div class="back__rule"></div>
    <p class="address">Your address, city<br>state, ZIP 0000</p>
  </section>
</body>
</html>
```